Movie Poster - The Vanity of Harbor Row

Need a movie poster for the independent film "The Vanity of Harbor Row". The film is a dark comedy/mockumentary about Wall Street.

Synopsis: In response to negative publicity; a prestigious Wall Street investment bank agrees to let an investigative journalist spend a day conducting interviews with their employees. The interview subjects include the bailout, the 2008 economic collapse, the mortgage crisis, DLMF, banker bonuses, the inequality of wealth, too big to fail banks, regulation of banks, tax rates, the Reclaim Copper Gate protestors and more.

You can see clips from the film and stills at www.thevanityofharborrow-film.example
The design will be used for the movie's poster which will be 27"x40", the dvd cover and various online and print formats.

Industry/Entity Type

Investment

Requirements
Must have
• The title of the film "The Vanity of Harbor Row"
The website www.thevanityofharborrow-film.example
A credit block
Starring: Carl Munday, Neil Ashcombe, Oliver Prynne, Gordon Whitlaw, Ralph Ketterby, Sam Voltin, Roy Talcott, Maren Dobbins, Lionel Ardanza, Dale Pemworth

Written & Directed by Neil Ashcombe

Director of Photography Curtis Halvey

Nice to have
• Using the attached photo in the design is preferred, but I'm willing to consider designs without it.

Some ideas that are optional: Title made out of $100 bills,
Wall Street Street sign, stock ticker, Copper Gate Stallion
The tagline which will be provided later.

```html
<!DOCTYPE html>
<html lang="en">
<head>
<meta charset="utf-8">
<title>The Vanity of Harbor Row — Poster</title>
<link rel="stylesheet" href="https://fonts.googleapis.com/css2?family=Oswald:wght@400;500&family=Arimo:wght@400&display=swap">
<style>
  :root {
    --ink: #050505;
    --band-dark: #2a2a2a;
    --band-grey: #9c9c9c;
    --flag-red: #c41f2b;
    --flag-white: #f1ece9;
    --flag-blue: #1d2660;
    --star: #f4f4f4;
    --bill-cream: #f1ebcd;
    --bill-shade: #ddd6b2;
    --bill-green: #3f4a3c;
    --title-cream: #e9e4cf;
    --credit-grey: #d0d0d0;
    --dollar-grey: #b8b8b8;
  }
  html, body { margin: 0; padding: 0; overflow: hidden; background: var(--ink); }
  .poster {
    position: relative;
    width: 810px;
    height: 1200px;
    overflow: hidden;
    background: var(--ink);
  }
  .poster-art { position: absolute; inset: 0; }
  .site-url {
    font-family: "Arimo", Arial, sans-serif;
    font-size: 31px;
    fill: #f2f2f2;
  }
  .dollar-mark {
    font-family: "Oswald", sans-serif;
    font-weight: 500;
    font-size: 70px;
    fill: var(--dollar-grey);
  }
  .bill { fill: url(#billTone); stroke: var(--bill-shade); stroke-width: 2; }
  .bill-frame { fill: none; stroke: var(--bill-green); stroke-width: 5; }
  .film-title {
    font-family: "Oswald", "Arial Narrow", sans-serif;
    font-weight: 500;
    font-size: 112px;
    fill: url(#titleFill);
  }
  .credits {
    position: absolute;
    left: 0;
    right: 0;
    top: 1012px;
    text-align: center;
    font-family: "Arimo", Arial, sans-serif;
    color: var(--credit-grey);
    font-size: 21px;
    line-height: 29px;
  }
  .credits p { margin: 0; }
  .credits .crew { margin-top: 14px; line-height: 30px; }
</style>
</head>
<body>
<div class="poster">
  <svg class="poster-art" width="810" height="1200" viewBox="0 0 810 1200" xmlns="http://www.w3.org/2000/svg">
    <defs>
      <linearGradient id="billTone" x1="0" y1="0" x2="1" y2="1">
        <stop offset="0" stop-color="var(--bill-cream)"/>
        <stop offset="1" stop-color="var(--bill-shade)"/>
      </linearGradient>
      <linearGradient id="castTone" x1="0" y1="0" x2="0" y2="1">
        <stop offset="0" stop-color="#a39d94"/>
        <stop offset="0.4" stop-color="#6f7480"/>
        <stop offset="0.7" stop-color="#2b2e38"/>
        <stop offset="1" stop-color="#15161c"/>
      </linearGradient>
      <linearGradient id="titleFill" x1="0" y1="0" x2="0" y2="1">
        <stop offset="0" stop-color="#f6f2e2"/>
        <stop offset="1" stop-color="#b7b49a"/>
      </linearGradient>
      <path id="star" d="M0,-12 L3.5,-4 L12,-3.7 L5.5,2 L7.4,11 L0,6 L-7.4,11 L-5.5,2 L-12,-3.7 L-3.5,-4 Z"/>
    </defs>

    <!-- flag: stripes -->
    <g class="flag" role="img" aria-label="American flag backdrop">
      <rect x="0" y="0" width="810" height="840" fill="var(--flag-white)"/>
      <rect x="0" y="0" width="810" height="58" fill="var(--flag-red)"/>
      <rect x="0" y="118" width="810" height="60" fill="var(--flag-red)"/>
      <rect x="0" y="238" width="810" height="60" fill="var(--flag-red)"/>
      <rect x="0" y="358" width="810" height="60" fill="var(--flag-red)"/>
      <rect x="0" y="478" width="810" height="60" fill="var(--flag-red)"/>
      <rect x="0" y="598" width="810" height="60" fill="var(--flag-red)"/>
      <rect x="0" y="718" width="810" height="60" fill="var(--flag-red)"/>
      <rect x="0" y="0" width="530" height="418" fill="var(--flag-blue)"/>
      <g fill="var(--star)">
        <use href="#star" x="300" y="60"/><use href="#star" x="380" y="60"/><use href="#star" x="460" y="60"/>
        <use href="#star" x="340" y="110"/><use href="#star" x="420" y="110"/><use href="#star" x="500" y="110"/>
        <use href="#star" x="380" y="160"/><use href="#star" x="460" y="160"/>
        <use href="#star" x="480" y="205"/>
        <use href="#star" x="38" y="308"/><use href="#star" x="78" y="350"/>
        <use href="#star" x="36" y="395"/>
      </g>
    </g>

    <!-- currency collage -->
    <g class="bill-collage" role="img" aria-label="Fanned stack of hundred dollar bills">
      <g transform="rotate(-8 150 420)">
        <rect class="bill" x="45" y="280" width="210" height="360"/>
        <rect class="bill-frame" x="60" y="295" width="180" height="330"/>
      </g>
      <g transform="rotate(-3 160 400)">
        <rect class="bill" x="80" y="255" width="200" height="330"/>
        <rect class="bill-frame" x="95" y="270" width="170" height="300"/>
      </g>
      <g transform="rotate(-4 600 400)">
        <rect class="bill" x="420" y="215" width="360" height="200"/>
        <rect class="bill-frame" x="435" y="230" width="330" height="170"/>
      </g>
      <g transform="rotate(6 620 500)">
        <rect class="bill" x="440" y="340" width="340" height="250"/>
        <rect class="bill-frame" x="455" y="355" width="310" height="220"/>
      </g>
      <g transform="rotate(-2 600 470)">
        <rect class="bill" x="420" y="330" width="300" height="270"/>
        <rect class="bill-frame" x="435" y="345" width="270" height="240"/>
      </g>
      <g transform="rotate(10 740 50)">
        <rect class="bill" x="680" y="-40" width="170" height="140"/>
        <rect class="bill-frame" x="692" y="-28" width="146" height="116"/>
      </g>
      <g transform="rotate(-30 790 560)">
        <rect class="bill" x="760" y="500" width="120" height="120"/>
      </g>
      <g transform="rotate(-20 0 610)">
        <rect class="bill" x="-40" y="585" width="60" height="50"/>
      </g>
    </g>

    <!-- lead cast photo -->
    <rect class="cast-photo" x="118" y="125" width="535" height="700" rx="40" fill="url(#castTone)" role="img" aria-label="Photo of a blonde woman in a grey suit standing behind a man in a dark suit and red tie holding a glass of champagne"/>

    <!-- top-left black corner with website band -->
    <polygon points="0,0 560,0 0,245" fill="var(--ink)"/>
    <polygon points="0,245 560,0 625,0 0,290" fill="var(--band-dark)"/>
    <polygon points="0,290 625,0 645,0 0,300" fill="var(--band-grey)"/>
    <text class="site-url" transform="translate(10,282) rotate(-25.5)">www.thevanityofharborrow-film.example</text>
    <text class="dollar-mark" x="36" y="108">$</text>
    <text class="dollar-mark" transform="translate(205,78) rotate(-28)" opacity="0.75">$</text>

    <!-- lower black field -->
    <polygon points="0,850 810,762 810,1200 0,1200" fill="var(--ink)"/>
    <polygon points="0,840 810,752 810,764 0,852" fill="var(--band-grey)"/>

    <text class="film-title" x="92" y="982" textLength="620" lengthAdjust="spacingAndGlyphs">The Vanity of Harbor Row</text>
  </svg>

  <div class="credits">
    <p>Starring: Carl Munday, Neil Ashcombe,</p>
    <p>Oliver Prynne, Gordon Whitlaw, Ralph Ketterby, Sam Voltin, Roy Talcott,</p>
    <p>Maren Dobbins, Lionel Ardanza, Dale Pemworth</p>
    <div class="crew">
      <p>Written &amp; Directed by:&nbsp;&nbsp;&nbsp; Neil Ashcombe</p>
      <p>Director of Photography Curtis Halvey</p>
    </div>
  </div>
</div>
</body>
</html>
```